R. K. Dalby, CPA & Associates, LLC
Your Accounting, Finance, and Tax Specialist
R. K. Dalby, CPA & Associates, LLC -
Use specific fonts
open to fonts
Professional
Rennick K. Dalby, CPA
President
4718 Copper Wren Ave. Harlow Bend, EQ 33952
rennickdalbycpa@mailnook.test

```html
<!DOCTYPE html>
<html lang="en">
<head>
<meta charset="utf-8">
<title>R. K. Dalby, CPA &amp; Associates, LLC — Stationery Set</title>
<link rel="stylesheet" href="https://fonts.googleapis.com/css2?family=Open+Sans:wght@400;600&display=swap">
<style>
  :root {
    --backdrop: #2d2d2f;
    --paper: #ffffff;
    --magenta-deep: #7a124d;
    --magenta: #b0246f;
    --blush: #e7a9c8;
    --ink: #4a4a4c;
    --card-dark: #353537;
    --envelope-grey: #a3a3a6;
    --envelope-grey-dark: #7e7e81;
    --flap-line: #d9d9db;
  }
  html, body {
    margin: 0;
    padding: 0;
    width: 1200px;
    height: 312px;
    overflow: hidden;
    background: var(--backdrop);
  }
  .stationery-set { display: block; width: 1200px; height: 312px; }
  .sheet { fill: var(--paper); }
  .sheet-dark { fill: var(--card-dark); }
  .brand-mark { fill: var(--magenta); }
  .brand-mark-light { fill: var(--paper); }
  .brand-name {
    font-family: "Open Sans", Arial, sans-serif;
    font-weight: 600;
    fill: var(--magenta-deep);
  }
  .brand-name-light { fill: var(--paper); }
  .contact {
    font-family: "Open Sans", Arial, sans-serif;
    font-weight: 400;
    fill: var(--ink);
  }
  .contact-light { fill: #d6d6d8; }
  .contact-name { font-weight: 600; fill: var(--magenta-deep); }
  .watermark { fill: none; stroke: var(--flap-line); stroke-width: 3; }
  .envelope-grey { fill: var(--envelope-grey); }
  .envelope-flap-grey { fill: var(--envelope-grey-dark); }
  .envelope-flap-line { fill: none; stroke: var(--flap-line); stroke-width: 1; }
  .swoosh-band { fill: url(#magentaBand); }
  .swoosh-line { fill: none; stroke: var(--blush); stroke-width: 0.8; }
</style>
</head>
<body>
<svg class="stationery-set" viewBox="0 0 1200 312" xmlns="http://www.w3.org/2000/svg">
  <defs>
    <linearGradient id="magentaBand" x1="0" y1="0" x2="1" y2="0">
      <stop offset="0" stop-color="#7a124d"/>
      <stop offset="0.6" stop-color="#a11f66"/>
      <stop offset="1" stop-color="#c02d7c"/>
    </linearGradient>
    <symbol id="headerSwoosh" viewBox="0 0 100 20" preserveAspectRatio="none">
      <path class="swoosh-band" d="M0 0 H100 V17 C72 5 38 9 0 12 Z"/>
      <path class="swoosh-line" d="M0 14 C38 11 70 7 100 19" vector-effect="non-scaling-stroke"/>
    </symbol>
  </defs>

  <!-- Business card: front -->
  <g class="business-card business-card-front" transform="translate(19 149)">
    <rect class="sheet" width="77" height="44"/>
    <use href="#headerSwoosh" width="77" height="9"/>
    <rect class="brand-mark" x="5" y="12" width="4" height="4"/>
    <text class="brand-name" x="11" y="15.4" font-size="3.3">R. K. Dalby, CPA &amp; Associates, LLC</text>
    <text class="contact contact-name" x="5" y="25" font-size="3.2">Rennick K. Dalby, CPA</text>
    <text class="contact" x="5" y="29" font-size="2.6">President</text>
    <text class="contact" x="5" y="35.5" font-size="2.4">4718 Copper Wren Ave. Harlow Bend, EQ 33952</text>
    <text class="contact" x="5" y="39.5" font-size="2.4">rennickdalbycpa@mailnook.test</text>
  </g>

  <!-- Business card: back -->
  <g class="business-card business-card-back" transform="translate(101 149)">
    <rect class="sheet-dark" width="77" height="44"/>
    <use href="#headerSwoosh" width="77" height="9"/>
    <rect class="brand-mark" x="8" y="21" width="4" height="4"/>
    <text class="brand-name brand-name-light" x="14" y="24.4" font-size="3.3">R. K. Dalby, CPA &amp; Associates, LLC</text>
  </g>

  <!-- Business card: alternate fronts -->
  <g class="business-card business-card-alt" transform="translate(19 202)">
    <rect class="sheet" width="77" height="44"/>
    <rect class="brand-mark" x="5" y="6" width="4" height="4"/>
    <text class="brand-name" x="11" y="9.4" font-size="3.3">R. K. Dalby, CPA &amp; Associates, LLC</text>
    <text class="contact contact-name" x="5" y="22" font-size="3.2">Rennick K. Dalby, CPA</text>
    <text class="contact" x="5" y="26" font-size="2.6">President</text>
    <text class="contact" x="5" y="35" font-size="2.4">rennickdalbycpa@mailnook.test</text>
  </g>
  <g class="business-card business-card-alt" transform="translate(101 202)">
    <rect class="sheet" width="77" height="44"/>
    <rect class="brand-mark" x="8" y="19" width="4" height="4"/>
    <text class="brand-name" x="14" y="22.4" font-size="3.3">R. K. Dalby, CPA &amp; Associates, LLC</text>
  </g>

  <!-- Letterhead: first page -->
  <g class="letterhead" transform="translate(197 24)">
    <rect class="sheet" width="228" height="276"/>
    <use href="#headerSwoosh" width="228" height="34"/>
    <rect class="brand-mark-light" x="62" y="5" width="5" height="5"/>
    <text class="brand-name brand-name-light" x="70" y="9.6" font-size="4.6">R. K. Dalby, CPA &amp; Associates, LLC</text>
    <circle class="watermark" cx="114" cy="200" r="42"/>
    <text class="contact" x="14" y="262" font-size="3.4">4718 Copper Wren Ave. Harlow Bend, EQ 33952</text>
    <text class="contact" x="14" y="267" font-size="3.4">rennickdalbycpa@mailnook.test</text>
  </g>

  <!-- Letterhead: second page -->
  <g class="letterhead" transform="translate(444 24)">
    <rect class="sheet" width="223" height="276"/>
    <use href="#headerSwoosh" width="223" height="34"/>
    <rect class="brand-mark-light" x="60" y="5" width="5" height="5"/>
    <text class="brand-name brand-name-light" x="68" y="9.6" font-size="4.6">R. K. Dalby, CPA &amp; Associates, LLC</text>
    <circle class="watermark" cx="111" cy="200" r="42"/>
  </g>

  <!-- Envelopes: front -->
  <g class="envelope envelope-front" transform="translate(679 29)">
    <rect class="sheet" width="233" height="127"/>
    <use href="#headerSwoosh" width="233" height="22"/>
    <rect class="brand-mark" x="10" y="26" width="5" height="5"/>
    <text class="brand-name" x="18" y="30.4" font-size="4.2">R. K. Dalby, CPA &amp; Associates, LLC</text>
    <text class="contact" x="10" y="39" font-size="3">4718 Copper Wren Ave.</text>
    <text class="contact" x="10" y="43" font-size="3">Harlow Bend, EQ 33952</text>
  </g>
  <g class="envelope envelope-front" transform="translate(679 163)">
    <rect class="sheet" width="233" height="125"/>
    <use href="#headerSwoosh" width="233" height="22"/>
    <rect class="brand-mark" x="10" y="26" width="5" height="5"/>
    <text class="brand-name" x="18" y="30.4" font-size="4.2">R. K. Dalby, CPA &amp; Associates, LLC</text>
    <text class="contact" x="10" y="39" font-size="3">4718 Copper Wren Ave.</text>
    <text class="contact" x="10" y="43" font-size="3">Harlow Bend, EQ 33952</text>
  </g>

  <!-- Envelopes: back -->
  <g class="envelope envelope-back" transform="translate(936 29)">
    <rect class="sheet" width="252" height="80"/>
    <path class="swoosh-band" d="M0 0 H252 L126 56 Z"/>
  </g>
  <g class="envelope envelope-back" transform="translate(936 110)">
    <rect class="envelope-grey" width="252" height="70"/>
    <path class="envelope-flap-grey" d="M0 0 H252 L126 46 Z"/>
  </g>
  <g class="envelope envelope-back" transform="translate(936 187)">
    <rect class="sheet" width="252" height="101"/>
    <path class="envelope-flap-line" d="M0 0 L126 52 L252 0 M0 101 L100 45 M252 101 L152 45"/>
  </g>
</svg>
</body>
</html>
```